Korvel Sense Social Media Advertisement

We need a social media advertisement made up for our Wealth Intelligence. Our initial campaign will be on Chatterly, so it needs to be compliant with chatterly. Attached is a brief, we just need 1 single design initially that we can interchange the copy to see what converts better. Must be in a format that we can easily edit. Attached also are some examples of advertisements that are currently posted on Chatterly for similar products. Moneyleaf is the closest competitor. Please visit our website: https://www.korvelsense.example to understand more about the business. You can also register as a free user to view the platform.

Target Market(s)

Self-directed Australian investors — particularly Self managed super fund trustees and property investors — who actively manage their own wealth and want AI-powered insights to make smarter financial decisions.

Industry/Entity Type

Financial technology (FinTech) / Wealth management software.

Requirements
Must have
• Dark, sophisticated colour palette (navy and teal), no emoji or decorative icons, clean and modern typography, and imagery that conveys intelligence, data, and financial confidence — not generic stock market clichés.
Nice to have
• Subtle futuristic or tech aesthetic, data visualisation elements (charts, graphs, network nodes), a sense of calm authority rather than aggressive "get rich" energy, and designs that would work across both digital ads and print formats.
Should not have
• Bright or garish colours, cartoonish illustrations, generic stock market imagery (bulls, bears, ticker tape), cluttered layouts, anything that feels salesy or hype-driven, and no cryptocurrency or "get rich quick" visual cues.

```html
<!DOCTYPE html>
<html lang="en">
<head>
<meta charset="utf-8">
<title>Korvel Sense – See Exactly When You Can Retire</title>
<link rel="stylesheet" href="https://fonts.googleapis.com/css2?family=Plus+Jakarta+Sans:wght@400;500;700;800&family=Inter:wght@400;500;600;700&family=JetBrains+Mono:wght@400;500;600&display=swap">
<style>
:root{
  --bg:#101b26;
  --bg-grid:rgba(255,255,255,.025);
  --panel:#0c1720;
  --panel-line:#1e2d38;
  --panel-border:#2b6e66;
  --teal:#2fd4b8;
  --teal-soft:#3fcfb4;
  --blue:#58a8e8;
  --white:#ffffff;
  --muted:#a9b3bd;
  --ui-text:#dfe6ec;
  --ui-muted:#7f8d99;
  --field:#0a141c;
  --amber:#e2b04a;
  --amber-bg:#33290f;
  --green:#5fd39a;
  --green-bg:#112a22;
  --green-line:#2a5d47;
  --chip-blue:#6aa6e0;
}
*{box-sizing:border-box;margin:0;padding:0}
html,body{width:1200px;height:1200px;overflow:hidden;background:var(--bg)}
.canvas{width:1200px;height:1200px;overflow:hidden;position:relative;background:var(--bg)}
.stage{position:absolute;left:0;top:0;width:1080px;height:1080px;transform:scale(1.11111);transform-origin:0 0;
  background:
    linear-gradient(var(--bg-grid) 1px,transparent 1px) 0 0/36px 36px,
    linear-gradient(90deg,var(--bg-grid) 1px,transparent 1px) 0 0/36px 36px,
    var(--bg);
  font-family:"Plus Jakarta Sans",sans-serif;overflow:hidden}
.brand{position:absolute;left:66px;top:42px;font-weight:700;font-size:33px;color:var(--white);letter-spacing:-.3px}
.headline{position:absolute;left:62px;top:152px;font-weight:700;font-size:78px;line-height:92px;color:var(--white);letter-spacing:-1px}
.headline .accent{background:linear-gradient(90deg,var(--teal) 0%,var(--teal) 45%,var(--blue) 75%);-webkit-background-clip:text;background-clip:text;color:transparent}
.points{position:absolute;left:64px;top:372px;list-style:none}
.points li{font-size:30px;color:var(--muted);line-height:59px;display:flex;align-items:center}
.points li::before{content:"";width:13px;height:13px;border-radius:50%;background:var(--teal);margin-right:13px}
.cta{position:absolute;left:63px;top:943px;width:207px;height:60px;border-radius:7px;background:var(--teal);color:#0b1a1f;font-weight:600;font-size:19px;display:flex;align-items:center;justify-content:center;box-shadow:0 6px 22px rgba(47,212,184,.25)}

.app{position:absolute;left:372px;top:407px;width:760px;height:720px;background:var(--panel);border:1.5px solid var(--panel-border);border-radius:16px;font-family:"Inter",sans-serif;color:var(--ui-text);overflow:hidden;box-shadow:0 0 40px rgba(47,212,184,.08)}
.app *{position:absolute}
.app .topbar{left:0;top:0;width:100%;height:56px;border-bottom:1px solid var(--panel-line)}
.menu-icon{left:28px;top:23px}
.topbar-title{left:54px;top:20px;font-size:12px;font-weight:600;color:var(--white)}
.feed-icon{left:18px;top:72px}
.feed-title{left:45px;top:69px;font-size:19px;font-weight:700;color:var(--white)}
.feed-sub{left:19px;top:95px;font-size:10.5px;color:var(--ui-muted)}
.tabs{left:0;top:148px;width:100%;height:1px;background:var(--panel-line)}
.tab{top:127px;font-size:10.5px;color:var(--ui-muted)}
.tab-count{position:static;display:inline-block;background:#1b2731;color:#667581;font-size:8.5px;padding:1px 5px;border-radius:6px;margin-left:4px}
.tab-active{left:165px;top:125px;width:121px;height:24px;border-bottom:2px solid var(--amber);color:#e8d29a;font-size:10.5px;padding-left:14px;padding-top:2px}
.tab-active svg{left:0;top:3px}

.field-label{left:31px;font-family:"JetBrains Mono",monospace;font-size:8px;letter-spacing:1.3px;color:var(--ui-muted)}
.field{left:31px;width:183px;height:28px;border:1px solid var(--panel-line);background:var(--field);border-radius:4px;font-size:9.5px;color:var(--ui-text);padding:8px 9px;border-bottom:2px solid #1c2a35}
.flag{position:static;display:inline-block;width:9px;height:7px;background:#b8c4d6;border-radius:1px;margin-right:5px;vertical-align:0}
.agent{left:31px;width:183px;height:25px;border:1px solid #1f4a44;background:#0d1d21;border-radius:4px;font-size:9.5px;color:#9fc7bd;padding:6px 0 0 25px}
.agent svg{left:8px;top:7px}
.agent .on{right:9px;left:auto;top:8px;font-family:"JetBrains Mono",monospace;font-size:6.5px;color:var(--teal)}
.deploy{left:31px;top:573px;width:183px;height:32px;background:var(--teal);border-radius:5px;color:#0b1a1f;font-size:10px;font-weight:600;padding:9px 0 0 62px}
.deploy svg{left:45px;top:11px}
.divider-v{left:227px;top:172px;width:1px;height:450px;background:var(--panel-line)}

.steps{left:243px;top:183px;display:flex;gap:4px;position:absolute}
.step{position:static;font-family:"JetBrains Mono",monospace;font-size:8px;color:#8fe0b2;border:1px solid var(--green-line);background:var(--green-bg);border-radius:3px;padding:2px 5px;white-space:nowrap}
.sep{position:static;color:#3e5160;font-size:8px;padding-top:3px}
.log{left:243px;font-family:"JetBrains Mono",monospace;font-size:8px;white-space:nowrap}
.results-tabs{left:228px;top:296px;width:560px;height:1px;background:var(--panel-line)}
.rtab{top:273px;font-size:9.5px;color:var(--ui-text)}
.rtab .count{position:static;display:inline-block;background:#173a33;color:var(--teal);font-size:8px;padding:0 5px;border-radius:6px;margin-left:4px}
.rtab-active{left:243px;width:128px;height:24px;border-bottom:2px solid var(--teal);padding-left:13px}
.rtab-active svg,.rtab-muted svg{left:0;top:1px}
.rtab-muted{left:386px;color:var(--ui-muted);padding-left:14px}
.rtab-muted .count{background:#1b2731;color:#7f8d99}
.found{left:243px;top:310px;font-size:11.5px;font-weight:700;color:var(--white)}

.card{left:243px;width:560px;border:1px solid var(--panel-line);border-radius:8px;background:#0e1a23}
.ticker{left:15px;width:43px;height:19px;border:1px solid #3a4955;border-radius:3px;font-family:"JetBrains Mono",monospace;font-size:9px;font-weight:600;color:var(--white);text-align:center;line-height:17px}
.co-name{left:66px;font-size:11px;font-weight:700;color:var(--white);line-height:13px;width:140px}
.badge{font-family:"JetBrains Mono",monospace;font-size:6.5px;color:var(--amber);background:var(--amber-bg);border:1px solid #6a5220;border-radius:2px;padding:1px 5px;white-space:nowrap}
.co-desc{left:66px;font-family:"JetBrains Mono",monospace;font-size:7.5px;line-height:9px;color:#8aa39b;width:130px}
.co-desc b{position:static;color:#b7e3cf;font-weight:500}
.tags{display:flex;gap:5px;position:absolute}
.tag{position:static;font-family:"JetBrains Mono",monospace;font-size:7px;white-space:nowrap;border-radius:2px;padding:2px 5px;border:1px solid var(--green-line);background:var(--green-bg);color:var(--green)}
.tag.warm{border-color:#6a5220;background:var(--amber-bg);color:var(--amber)}
.tag.cool{border-color:#2b4d70;background:#0f2133;color:var(--chip-blue)}
</style>
</head>
<body>
<div class="canvas">
<div class="stage">
  <div class="brand">Korvel Sense</div>
  <h1 class="headline">See Exactly When<br><span class="accent">You Can Retire.</span></h1>
  <ul class="points">
    <li>Model it.</li>
    <li>Track it.</li>
    <li>Own it.</li>
  </ul>
  <div class="cta">Explore Platform</div>

  <div class="app">
    <div class="topbar">
      <svg class="menu-icon" width="12" height="9" viewBox="0 0 12 9"><path d="M0 .5h12M0 4.5h12M0 8.5h12" stroke="#7f8d99" stroke-width="1.2"/></svg>
      <div class="topbar-title">Intelligence</div>
    </div>
    <svg class="feed-icon" width="18" height="20" viewBox="0 0 18 20"><path d="M10 1 2 12h7l-1 7 8-11H9z" fill="none" stroke="#2fd4b8" stroke-width="1.6" stroke-linejoin="round"/></svg>
    <div class="feed-title">Intelligence Feed</div>
    <div class="feed-sub">Screen for growth opportunities across your watchlist and market</div>

    <div class="tab" style="left:19px">Feed<span class="tab-count">50</span></div>
    <div class="tab" style="left:113px">Signals</div>
    <div class="tab-active"><svg width="9" height="9" viewBox="0 0 9 9"><circle cx="4" cy="4" r="3" fill="none" stroke="#e8d29a" stroke-width="1.1"/><path d="m6.2 6.2 2.3 2.3" stroke="#e8d29a" stroke-width="1.1"/></svg>Growth Scanner</div>
    <div class="tabs"></div>

    <div class="field-label" style="top:189px">MARKET</div>
    <div class="field" style="top:203px"><span class="flag"></span>USA (Main Exchanges)</div>
    <div class="field-label" style="top:246px">SECTOR</div>
    <div class="field" style="top:260px">AI Infrastructure</div>
    <div class="field-label" style="top:299px">MARKET CAP RANGE</div>
    <div class="field" style="top:313px">Small ($300M – $2B)</div>
    <div class="field-label" style="top:352px">MIN ERS SCORE</div>
    <div class="field" style="top:366px">90+ Exceptional</div>
    <div class="field-label" style="top:405px">RESEARCH AGENTS</div>

    <div class="agent" style="top:418px"><svg width="10" height="10" viewBox="0 0 10 10"><path d="M1 3V1h2M7 1h2v2M9 7v2H7M3 9H1V7" fill="none" stroke="#6fb8a8" stroke-width="1"/></svg>Sector Scanner<span class="on">ON</span></div>
    <div class="agent" style="top:447px"><svg width="10" height="10" viewBox="0 0 10 10"><path d="M2 9V5M5 9V1M8 9V6" stroke="#6fb8a8" stroke-width="1.2"/></svg>Fundamentals<span class="on">ON</span></div>
    <div class="agent" style="top:476px"><svg width="10" height="10" viewBox="0 0 10 10"><path d="M2 1h4l2 2v6H2z M4 5h3M4 7h3" fill="none" stroke="#6fb8a8" stroke-width="1"/></svg>Regulatory Filings<span class="on">ON</span></div>
    <div class="agent" style="top:505px"><svg width="10" height="10" viewBox="0 0 10 10"><circle cx="5" cy="5" r="4" fill="none" stroke="#6fb8a8"/><path d="M1 5h8M5 1c2 2 2 6 0 8M5 1c-2 2-2 6 0 8" fill="none" stroke="#6fb8a8" stroke-width=".8"/></svg>Macro Tailwinds<span class="on">ON</span></div>
    <div class="agent" style="top:534px"><svg width="10" height="10" viewBox="0 0 10 10"><path d="M6 0 2 6h3l-1 4 4-6H5z" fill="none" stroke="#6fb8a8" stroke-width=".9"/></svg>ERS Scorer<span class="on">ON</span></div>
    <div class="deploy"><svg width="9" height="9" viewBox="0 0 9 9"><circle cx="4" cy="4" r="3" fill="none" stroke="#0b1a1f" stroke-width="1.2"/><path d="m6.2 6.2 2.3 2.3" stroke="#0b1a1f" stroke-width="1.2"/></svg>Deploy Agents</div>
    <div class="divider-v"></div>

    <div class="steps">
      <span class="step">✓ Sector Scanner</span><span class="sep">›</span>
      <span class="step">✓ Fundamentals</span><span class="sep">›</span>
      <span class="step">✓ Regulatory Filings</span><span class="sep">›</span>
      <span class="step">✓ Macro Tailwinds</span><span class="sep">›</span>
      <span class="step">✓ ERS Scorer</span>
    </div>
    <div class="log" style="top:206px;color:#9fb0bb">[ERS Scorer] Final ranking complete — candidates returned.</div>
    <div class="log" style="top:220px;color:#5f6f7b">[Scorer] Calling synthesis model…</div>
    <div class="log" style="top:235px;color:#8fe0b2">[Scorer] 3 candidates above threshold — complete.</div>

    <div class="rtab rtab-active"><svg width="10" height="10" viewBox="0 0 10 10"><path d="M1 3V1h2M7 1h2v2M9 7v2H7M3 9H1V7" fill="none" stroke="#cfd8de" stroke-width="1"/></svg>Scan Results<span class="count">3</span></div>
    <div class="rtab rtab-muted"><svg width="10" height="10" viewBox="0 0 10 10"><rect x="1.5" y="1" width="7" height="8" rx="1" fill="none" stroke="#7f8d99"/></svg>Watchlist<span class="count">6</span></div>
    <div class="results-tabs"></div>
    <div class="found">3 candidates identified</div>

    <div class="card" style="top:326px;height:79px">
      <div class="ticker" style="top:30px">VRTN</div>
      <div class="co-name" style="top:10px">Veritan Group N.V.</div>
      <div class="badge" style="left:66px;top:26px">⚡ FOUNDER</div>
      <div class="co-desc" style="top:40px">AI Infrastructure <b>◆</b><br>Switching Costs ·<br>emerging</div>
      <div class="tags" style="left:187px;top:33px"><span class="tag">REV ACCEL +479% YOY</span><span class="tag warm">HYPERSCALER ANCHOR DEALS</span><span class="tag cool">NORVEX STAKE</span></div>
    </div>
    <div class="card" style="top:412px;height:65px">
      <div class="ticker" style="top:22px">CLDR</div>
      <div class="co-name" style="top:10px">Calder Technology Group Holding Ltd</div>
      <div class="co-desc" style="top:37px;width:160px">AI Infrastructure <b>◆ Intangible</b><br>Assets · <b>strong</b></div>
      <div class="tags" style="left:225px;top:27px"><span class="tag">REV ACCEL +201% YOY</span><span class="tag">67%+ GROSS MARGIN</span><span class="tag warm">HYPERSCALE DEMAND</span></div>
    </div>
    <div class="card" style="top:483px;height:57px">
      <div class="ticker" style="top:18px">IDXD</div>
      <div class="co-name" style="top:10px;width:auto;white-space:nowrap">Indexa Data Inc.</div>
      <div class="badge" style="left:160px;top:11px">⚡ FOUNDER</div>
      <div class="co-desc" style="top:25px;width:170px">AI Infrastructure <b>◆</b> Switching<br>Costs · emerging</div>
      <div class="tags" style="left:243px;top:22px"><span class="tag">REV ACCEL +48% FY2025</span><span class="tag">96% YOY FY2024</span><span class="tag warm">5 OF TOP 7</span></div>
    </div>
  </div>
</div>
</div>
</body>
</html>
```